Exclusive beauty salon needs a price list or services booklet

I need a new very attractive flyer for my beauty salon, containing information on the different services and their prices.
In attachment you can find a pdf of the "old" one, but I'd love to have a beautifully designed new one!
I'd love to have a booklet in format 148 x 148 mm, or in US format, containing 12 or 16 pages, but if you can offer other nice looking designs they are welcome!
The services that need to come in the booklet with their prices can all be found on my website: www.atelierkova.be, starting with
Gelaatsverzorging
Wimperverlenging
Suikerontharing
Wimperlifting
Permanente Make Up
Airbrush Tanning

Target Market(s)

woman from 20 to 89 years old

Industry/Entity Type

Beauty Salon

Font styles to use
Sans Serif

Colors

Designer to choose colors to be used in the design.

Requirements
Must have
• a classy nice look, it must contain details about the services from my beauty salon and their prices, and nice pictures.
• The Names, prices and explanations of the services can easily be found on my website: www.atelierkova.be
Nice to have
• In attachment you can find the "old" price list in pdf, what I need now is a "new booklet" with the new logo and updated services price list.
• I need a very nice and attractive looking booklet, classy chique, Paris chique, looking very expensive.
Should not have
• Not too much colors, not too curly, but still feminine

```html
<!DOCTYPE html>
<html lang="nl">
<head>
<meta charset="utf-8">
<title>Wimperlift – behandeling</title>
<link href="https://fonts.googleapis.com/css2?family=Didact+Gothic&family=Lora:wght@400;500&display=swap" rel="stylesheet">
<style>
  :root{
    --stage:#d4d4d4;
    --page-left:#efefef;
    --page-right:#fbfbfb;
    --rose:#d898a3;
    --rose-soft:#e4b3bb;
    --band:#d696a1;
    --band-light:#e2aab3;
    --ink:#2b2b2b;
    --band-ink:#2a2226;
  }
  *{box-sizing:border-box;margin:0;padding:0}
  html,body{width:1200px;height:900px;overflow:hidden}
  body{background:var(--stage);position:relative;font-family:"Didact Gothic",sans-serif;color:var(--ink)}
  .spread{position:absolute;left:117px;top:174px;width:966px;height:553px;display:flex;box-shadow:0 2px 6px rgba(0,0,0,.12)}
  .page{position:relative;width:483px;height:553px;overflow:hidden}
  .page--left{background:linear-gradient(90deg,var(--page-left) 0%,#f4f4f4 88%,#e3e3e3 100%)}
  .page--right{background:linear-gradient(90deg,#e6e6e6 0%,var(--page-right) 10%,var(--page-right) 100%)}
  .column{position:absolute;top:18px;width:190px}
  .page--left .column:nth-child(1){left:40px}
  .page--left .column:nth-child(2){left:252px;width:200px}
  .page--right .column:nth-child(1){left:38px;width:186px}
  .page--right .column:nth-child(2){left:272px;width:196px}
  .icon{display:block;margin:0 auto;height:80px;width:100px}
  .column-title{font-family:"Lora",serif;font-weight:400;color:var(--rose);font-size:15px;text-align:center;margin:24px 0 14px}
  .column-text{font-size:8.2px;line-height:1.85;text-align:justify}
  .column-text p{margin:0}
  .band{position:absolute;left:0;top:424px;width:100%;height:88px;
    background:linear-gradient(100deg,var(--band) 0%,var(--band-light) 45%,var(--band) 100%)}
  .band-content{position:absolute;left:0;top:424px;width:100%;height:88px;text-align:center;padding-top:16px}
  .band-title{font-family:"Lora",serif;font-weight:500;font-size:14.5px;color:var(--band-ink);margin-bottom:7px}
  .band-text{font-size:11.5px;line-height:1.35;color:var(--band-ink);margin:0 auto;width:400px}
</style>
</head>
<body>
<main class="spread">
  <section class="page page--left">
    <article class="column">
      <svg class="icon" viewBox="0 0 100 80" aria-hidden="true">
        <g fill="none" stroke="var(--rose)" stroke-width="2.4" stroke-linecap="round" stroke-linejoin="round">
          <rect x="31" y="8" width="38" height="66" rx="2"/>
          <rect x="42" y="4" width="16" height="8" rx="1.5" fill="var(--rose)"/>
          <path d="M37 24l3 3 5-6M37 36l3 3 5-6M37 48l3 3 5-6M37 60l3 3 5-6"/>
          <path d="M50 25h13M50 37h13M50 49h13M50 61h13"/>
        </g>
      </svg>
      <h2 class="column-title">Voorbereiding</h2>
      <div class="column-text">
        <p>Er wordt een referentiekaart aangemaakt waarop al uw gegevens staan, hierop staan ook gedetailleerde gegevens over de behandeling en mogelijke allergieën waar u last van heeft en eventueel de uitslagen van een algemene test patch.</p>
        <p>Er wordt indien gewenst een voor en na foto gemaakt.</p>
        <p>Indien u contactlenzen draagt dient u deze voorafgaand aan de behandeling te verwijderen.</p>
        <p>Je kan best geen mascara aandoen om op uw afspraak te komen, dit komt het resultaat van de wimperlifting ten goede.</p>
        <p>De wimpers worden met een speciale cleanser schoongemaakt.</p>
      </div>
    </article>
    <article class="column">
      <svg class="icon" viewBox="0 0 100 80" aria-hidden="true">
        <g fill="none" stroke="var(--rose)" stroke-linecap="round">
          <path d="M20 32 Q50 14 80 30" stroke-width="4"/>
          <path d="M18 44 Q50 64 82 44" stroke-width="3.5"/>
          <path d="M28 52l-4 6M37 56l-2 7M46 58l-1 7M55 58l1 7M64 56l2 7M73 52l4 6" stroke-width="2"/>
        </g>
      </svg>
      <h2 class="column-title">De behandeling zelf</h2>
      <div class="column-text">
        <p>De onderste wimpers worden afgedekt met speciale patches om te voorkomen dat deze vastplakken aan de siliconen pads, u dient uw ogen gesloten te houden gedurende de behandeling.</p>
        <p>Er wordt bepaald welke siliconen pads het meest geschikt zijn voor uw wimpers en deze worden bevestigd op uw ooglid.</p>
        <p>De wimperhaartjes worden één voor één bevestigd op de siliconen pads.</p>
        <p>De wimperlift wordt in drie fasen aangebracht (de inwerktijden zijn afhankelijk van de lengte en dikte van uw wimpers).</p>
      </div>
    </article>
    <div class="band" role="img" aria-label="Roze band met zacht bloemenpatroon"></div>
    <div class="band-content">
      <h3 class="band-title">Einde van de behandeling.</h3>
      <p class="band-text">De siliconen patches worden losgemaakt van uw oogleden en uw wimpers worden gekamd.</p>
    </div>
  </section>

  <section class="page page--right">
    <article class="column">
      <svg class="icon" viewBox="0 0 100 80" aria-hidden="true">
        <path d="M70 16 A30 30 0 1 1 50 10" fill="none" stroke="var(--rose)" stroke-width="5" stroke-linecap="round"/>
        <path d="M60 2 L74 14 L58 20 Z" fill="var(--rose)"/>
        <text x="50" y="51" text-anchor="middle" font-family="Didact Gothic, sans-serif" font-size="26" font-weight="700" fill="var(--rose)">48</text>
      </svg>
      <h2 class="column-title">Enkele feiten</h2>
      <div class="column-text">
        <p>De wimperlift is een behandeling die de NATUURLIJKE wimpers lift en deze een boost geeft.</p>
        <p>De behandeling duurt slechts 45 - 60 minuten en wordt als zeer comfortabel ervaren.</p>
        <p>Het effect van de wimperlift behandeling blijft tussen de 4 à 6 weken zichtbaar, dit is de natuurlijke levenscyclus van een wimper.</p>
        <p>De behandeling heeft een verhelderend en liftend effect van de huid rond de ogen.</p>
        <p>De wimpers worden gekleurd zodat de natuurlijke schoonheid en kleur nog meer wordt versterkt.</p>
      </div>
    </article>
    <article class="column">
      <svg class="icon" viewBox="0 0 100 80" aria-hidden="true">
        <g fill="none" stroke="var(--rose)" stroke-linecap="round">
          <path d="M24 16 Q52 4 84 20" stroke-width="4"/>
          <path d="M26 44 Q54 16 84 40 Q54 66 26 44 Z" stroke-width="2.5"/>
          <circle cx="55" cy="42" r="11" stroke-width="2.5"/>
          <path d="M28 42l-12 -6M27 38l-10 -10M30 34l-6 -12M34 30l-2 -12" stroke-width="2"/>
        </g>
        <circle cx="55" cy="42" r="5" fill="var(--rose)"/>
      </svg>
      <h2 class="column-title">Het effect: wimperlift</h2>
      <div class="column-text">
        <p>Je eigen wimpers krijgen een mooie krul, het resultaat is bij iedereen uniek, aangezien het volledig afhankelijk is van de lengte van je eigen wimpers. Het resultaat moet zo'n zes weken blijven, dan pas mag je een nieuwe behandeling laten uitvoeren. Het effect verliest zijn kracht naarmate de zes weken naderen, je wimpers krijgen weer hun natuurlijke krul terug na zo'n acht weken. Ondertussen zijn er al veel nieuwe wimpers gegroeid.</p>
      </div>
    </article>
    <div class="band" role="img" aria-label="Roze band met zacht bloemenpatroon"></div>
    <div class="band-content">
      <h3 class="band-title">Einde van de behandeling.</h3>
      <p class="band-text">U mag direct na de behandeling niet in uw ogen wrijven en gedurende 48 u niet in contact komen met water.</p>
    </div>
  </section>
</main>
</body>
</html>
```